Bay & Meadow Property Services Tri-fold sales & marketing brochure

We need a tri-fold brochure that describes our three lines of business and the various services within each line to use in sales and marketing efforts.
See website for additional background info:
https://halvernq7.example-host.com/

Target Market(s)

Real Estate Investors & owners in Residential Rental, Short-term Rentals, and Mini/Maxi Storage Rental markets

Requirements
Must have
• See attached logo, use color scheme & font styles to match. Make sure to utilize photos to enhance look/feel.

```html
<!DOCTYPE html>
<html lang="en">
<head>
<meta charset="utf-8">
<title>Bay &amp; Meadow Property Services – Tri-fold Brochure</title>
<link href="https://fonts.googleapis.com/css2?family=Montserrat:wght@400;600;700;800&family=Playfair+Display:ital,wght@0,600;1,600&display=swap" rel="stylesheet">
<style>
:root{
  --navy:#0d1a2b;
  --navy-2:#16283f;
  --teal:#1ea9cc;
  --teal-dark:#137f9c;
  --cyan:#3cc3e3;
  --paper:#ffffff;
  --ink:#2b3340;
  --muted:#6a7482;
  --backdrop:#e8eaed;
}
*{box-sizing:border-box;margin:0;padding:0}
html,body{width:863px;height:1200px;overflow:hidden}
body{background:var(--backdrop);font-family:"Montserrat",Arial,sans-serif;color:var(--ink);position:relative}
.spread{position:absolute;left:58px;width:748px;display:flex;box-shadow:0 4px 14px rgba(0,0,0,.18)}
.spread--outside{top:40px;height:600px}
.spread--inside{top:668px;height:510px;background:var(--paper);overflow:hidden}
.panel{position:relative;width:249.33px;height:100%;overflow:hidden}

/* About panel */
.about{background:var(--navy);color:#dfe6ee}
.about .photo{height:150px;background:linear-gradient(135deg,#12314a,#1c6f8e 60%,#0e2236)}
.about .body{padding:18px 20px}
.about h2{font-size:15px;font-weight:800;color:#fff;letter-spacing:.5px;margin-bottom:8px}
.about p{font-size:7px;line-height:1.6;margin-bottom:8px}
.about h3{font-size:8px;color:var(--teal);font-weight:700;margin:10px 0 6px}

/* Contact panel */
.contact{background:linear-gradient(180deg,var(--cyan),var(--teal) 55%,var(--teal-dark));color:#fff;text-align:center}
.contact .photo{position:absolute;left:28px;top:110px;width:193px;height:140px;border:5px solid #fff;background:linear-gradient(180deg,#cfdce6,#8e9aa5 60%,#5b6670)}
.contact .block{position:absolute;left:0;right:0;top:300px}
.contact h2{font-size:17px;font-weight:800;letter-spacing:1px}
.contact .phone{font-size:14px;font-weight:700;margin:8px 0 6px}
.contact .line{font-size:7px;line-height:1.7}
.contact .base{position:absolute;left:0;right:0;bottom:0;height:150px;background:var(--navy)}

/* Cover panel */
.cover{background:var(--paper)}
.brand{display:flex;align-items:center;gap:8px;padding:26px 22px 0}
.brand .mark{width:30px;height:30px;border-radius:50%;background:var(--navy)}
.brand .name{font-size:11px;font-weight:700;color:var(--navy);line-height:1.2}
.cover .headline{text-align:center;font-size:15px;font-weight:800;color:var(--teal);line-height:1.25;margin:20px 18px 14px}
.cover .photo{height:150px;margin:0 0 0 0;background:linear-gradient(135deg,#d9dde1,#f3f4f5 45%,#9aa6b1)}
.cover .lower{position:absolute;left:0;right:0;bottom:0;height:270px;background:var(--navy);padding:34px 22px}
.lines{list-style:none}
.lines li{display:flex;align-items:center;gap:8px;color:#fff;font-size:8.5px;font-weight:700;margin-bottom:9px;letter-spacing:.3px}
.lines svg{flex:none}
.phone-tag{position:absolute;left:22px;right:22px;bottom:30px;height:36px;background:var(--teal);color:#fff;font-weight:800;font-size:15px;display:flex;align-items:center;justify-content:center}

/* Inside */
.inside-top{position:absolute;left:0;top:0;width:748px;height:34px}
.inside-bottom{position:absolute;left:0;bottom:0;width:748px;height:72px}
.service{padding:48px 20px 0}
.service .title{display:flex;align-items:center;gap:8px;height:40px}
.service .title .dot{width:22px;height:22px;border-radius:50%;background:var(--teal);flex:none}
.service .title h2{font-family:"Playfair Display",Georgia,serif;font-style:italic;font-size:13px;color:var(--teal-dark);line-height:1.15;text-transform:uppercase}
.service .photo{height:105px;margin:10px 0 12px}
.service h3{font-size:9px;font-weight:800;color:var(--navy);line-height:1.3;margin-bottom:8px}
.service h4{font-size:6.5px;font-weight:700;color:var(--navy);margin-top:5px}
.service p{font-size:6px;line-height:1.5;color:var(--muted)}
.photo--home{background:linear-gradient(180deg,#b9d3e4,#e2e7ea 55%,#7d8f76)}
.photo--coast{background:linear-gradient(180deg,#8fd2ec,#4fb3d6 50%,#e6d6b5)}
.photo--storage{background:linear-gradient(180deg,#cfe1ee,#eef1f3 50%,#9aa3ab)}
.inside-phone{position:absolute;left:20px;bottom:16px;width:150px;height:30px;background:var(--teal);color:#fff;font-weight:800;font-size:13px;display:flex;align-items:center;justify-content:center}
.inside-contact{position:absolute;right:24px;bottom:16px;color:#fff;font-size:8px;line-height:1.6;text-align:left}
</style>
</head>
<body>

<section class="spread spread--outside">
  <article class="panel about">
    <div class="photo" role="img" aria-label="Hand touching a row of glowing business icons"></div>
    <div class="body">
      <h2>ABOUT US</h2>
      <p>Whether you own a single rental or a growing portfolio, our team helps investors find, manage and grow property that pays. We bring local insight and steady care to every home, suite and unit we handle.</p>
      <p>We tailor each plan to your goals so your assets stay filled, cared for and earning well over the long run.</p>
      <h3>Our Services Include:</h3>
      <p>Investment Opportunity Evaluation: Finding and reviewing homes and sites with strong returns for each owner.</p>
      <p>Rental Property Management: Tenant screening, rent collection, upkeep and clear monthly reporting.</p>
      <p>Development &amp; Renovation Advice: Guidance on updates that lift value and attract quality renters.</p>
      <p>Storage Facility Oversight: Unit leasing, pricing reviews and site care for mini and maxi storage owners.</p>
      <p>We keep owners informed with simple reports, quick answers and a plan that grows with them.</p>
    </div>
  </article>

  <article class="panel contact">
    <div class="photo" role="img" aria-label="Modern storage building with roll-up doors"></div>
    <div class="block">
      <h2>CONTACT US</h2>
      <div class="phone">(555) 214-3088</div>
      <div class="line">info@bayandmeadowproperty.example</div>
      <div class="line">www.bayandmeadowproperty.example</div>
    </div>
  </article>

  <article class="panel cover">
    <div class="brand">
      <span class="mark"></span>
      <span class="name">Bay &amp; Meadow<br>Property Services</span>
    </div>
    <h1 class="headline">WHERE EXPERTISE MEETS<br>EXCEPTIONAL RETURNS</h1>
    <div class="photo" role="img" aria-label="Hand holding a small house model with keys"></div>
    <div class="lower">
      <ul class="lines">
        <li><svg width="12" height="12" viewBox="0 0 12 12"><rect width="12" height="12" fill="#1ea9cc"/><path d="M3 6.2l2 2 4-4.4" stroke="#fff" stroke-width="1.6" fill="none"/></svg>LONG-TERM RESIDENTIAL RENTALS</li>
        <li><svg width="12" height="12" viewBox="0 0 12 12"><rect width="12" height="12" fill="#1ea9cc"/><path d="M3 6.2l2 2 4-4.4" stroke="#fff" stroke-width="1.6" fill="none"/></svg>SHORT-TERM VACATION RENTALS</li>
        <li><svg width="12" height="12" viewBox="0 0 12 12"><rect width="12" height="12" fill="#1ea9cc"/><path d="M3 6.2l2 2 4-4.4" stroke="#fff" stroke-width="1.6" fill="none"/></svg>STORAGE FACILITY SERVICES</li>
      </ul>
      <div class="phone-tag">(555) 214-3088</div>
    </div>
  </article>
</section>

<section class="spread spread--inside">
  <svg class="inside-top" viewBox="0 0 748 34" preserveAspectRatio="none">
    <path d="M0 0H748V10C560 30 260 -4 0 22Z" fill="#0d1a2b"/>
    <path d="M0 22C260 -4 560 30 748 10V14C560 34 260 2 0 26Z" fill="#1ea9cc"/>
  </svg>

  <article class="panel service">
    <div class="title"><span class="dot"></span><h2>Long-Term<br>Residential Rentals</h2></div>
    <div class="photo photo--home" role="img" aria-label="Suburban family home with a green lawn"></div>
    <h3>LOCATE HIGH-VALUE RESIDENTIAL INVESTMENT OPPORTUNITIES</h3>
    <h4>Market Research &amp; Analysis</h4>
    <p>Study local trends, rents and vacancy to spot homes with steady demand.</p>
    <h4>Property Acquisition Support</h4>
    <p>Guide offers, inspections and closing so each buy fits your plan.</p>
    <h4>Tenant Placement</h4>
    <p>Market listings, screen applicants and sign clear, fair leases.</p>
    <h4>Ongoing Management</h4>
    <p>Handle rent, repairs and renewals while you track results monthly.</p>
  </article>

  <article class="panel service">
    <div class="title"><span class="dot"></span><h2>Short-Term<br>Vacation Rentals</h2></div>
    <div class="photo photo--coast" role="img" aria-label="Vacation rental home by the water"></div>
    <h3>UNLOCK HIDDEN POTENTIAL IN THE SHORT-TERM RENTAL MARKET</h3>
    <h4>Location &amp; Revenue Review</h4>
    <p>Find towns and homes where guests book often and nightly rates stay high.</p>
    <h4>Setup &amp; Furnishing</h4>
    <p>Design inviting spaces, stock supplies and prepare listing photos.</p>
    <h4>Booking Management</h4>
    <p>Set smart pricing, answer guests and keep calendars full all season.</p>
    <h4>Cleaning &amp; Upkeep</h4>
    <p>Coordinate turnovers and quick fixes so every stay earns top reviews.</p>
  </article>

  <article class="panel service">
    <div class="title"><span class="dot"></span><h2>Storage Facility<br>Services</h2></div>
    <div class="photo photo--storage" role="img" aria-label="Row of self-storage units with roll-up doors"></div>
    <h3>MINI-MAXI STORAGE: DISCOVER UNTAPPED POTENTIAL IN THE MINI &amp; MAXI STORAGE MARKET</h3>
    <h4>Location Review</h4>
    <p>Assess traffic, access and local demand before you build or buy.</p>
    <h4>Facility Planning</h4>
    <p>Plan unit mix, layout and security to match renter needs.</p>
    <h4>Leasing &amp; Pricing</h4>
    <p>Fill units fast with online rentals and rates that track the market.</p>
    <h4>Site Management</h4>
    <p>Oversee gates, upkeep and billing for smooth daily operation.</p>
  </article>

  <svg class="inside-bottom" viewBox="0 0 748 72" preserveAspectRatio="none">
    <path d="M0 20C250 0 520 34 748 8V14C520 40 250 6 0 26Z" fill="#1ea9cc"/>
    <path d="M0 26C250 6 520 40 748 14V72H0Z" fill="#0d1a2b"/>
  </svg>
  <div class="inside-phone">(555) 214-3088</div>
  <div class="inside-contact">info@bayandmeadowproperty.example<br>www.bayandmeadowproperty.example</div>
</section>

</body>
</html>
```